Lanternwake Tales - A podcast of inspiring stories of people living a heart centred life

We need a thumbnail to use on Podvane for our podcast 'Lanternwake Tales'.

Each week Rosalind Pettigrew & Wendy Tulloch interview inspirational people who have come from a place of adversity to living a truly inspired life.

From animal healing to breaking through the lowest of lows - Lanternwake tales brings together people who are on a journey living a heart centred life.

Purples, greens, yellows, and pinks are our preference.

Reason: The designs provided aren't appropriate. Elegant and Professional is what we're after.

Target Market(s)

People searching for meaning in life - self help book readers.

Colors
33b8a4
abd037
fbee3e
ffcf3e
faa54b
fef6f0
f04a50
e34197
f37122

Requirements
Must have
• Striking colours.
Nice to have
• Blended colours are preferred over blocks. But we're open to suggestions.
Should not have
• Overused podcast themes.

```html
<!DOCTYPE html>
<html lang="en">
<head>
<meta charset="utf-8">
<title>Lanternwake Tales – Podcast Cover</title>
<link rel="stylesheet" href="https://fonts.googleapis.com/css2?family=Marcellus&display=swap">
<style>
  :root {
    --bg: #f2f2f2;
    --haze: #ffffff;
    --red: #f04a50;
    --pink: #e34197;
    --mauve: #a2628c;
    --slate: #7b7a8c;
    --teal: #33b8a4;
    --green: #4ccf5a;
    --lime: #abd037;
    --yellow: #fbee3e;
    --amber: #ffcf3e;
    --orange: #faa54b;
    --cream: #fef6f0;
  }
  * { margin: 0; padding: 0; box-sizing: border-box; }
  html, body {
    width: 1200px;
    height: 1200px;
    overflow: hidden;
    background: var(--bg);
  }
  .cover {
    position: relative;
    width: 1200px;
    height: 1200px;
    overflow: hidden;
    background:
      radial-gradient(ellipse 60% 40% at 30% 30%, var(--haze) 0%, rgba(255,255,255,0) 70%),
      radial-gradient(ellipse 50% 40% at 80% 55%, var(--haze) 0%, rgba(255,255,255,0) 70%),
      var(--bg);
  }
  .cover__title {
    position: absolute;
    top: 40px;
    left: 0;
    width: 1200px;
    text-align: center;
    font-family: "Marcellus", serif;
    font-weight: 400;
    text-transform: uppercase;
    line-height: 1;
  }
  .cover__title-line {
    display: block;
    white-space: nowrap;
    font-size: 146px;
    letter-spacing: -1px;
    -webkit-background-clip: text;
    background-clip: text;
    color: transparent;
  }
  .cover__title-line--main {
    background-image: linear-gradient(90deg, var(--red) 0%, var(--pink) 22%, #d2478a 45%, var(--slate) 62%, var(--teal) 80%, var(--green) 100%);
  }
  .cover__title-line--sub {
    margin-top: 8px;
    background-image: linear-gradient(90deg, var(--pink) 30%, var(--mauve) 50%, var(--slate) 60%, var(--teal) 72%);
  }
  .cover__hands {
    position: absolute;
    left: 100px;
    top: 345px;
    width: 1025px;
    height: 855px;
    border-radius: 46% 46% 0 0 / 30% 30% 0 0;
    background:
      radial-gradient(ellipse 30% 25% at 22% 18%, var(--lime) 0%, rgba(171,208,55,0) 100%),
      radial-gradient(ellipse 25% 25% at 10% 40%, var(--teal) 0%, rgba(51,184,164,0) 100%),
      radial-gradient(ellipse 35% 25% at 60% 22%, var(--pink) 0%, rgba(227,65,151,0) 100%),
      radial-gradient(ellipse 25% 20% at 22% 55%, var(--pink) 0%, rgba(227,65,151,0) 100%),
      radial-gradient(ellipse 35% 35% at 82% 45%, var(--orange) 0%, rgba(250,165,75,0) 100%),
      radial-gradient(ellipse 55% 25% at 50% 100%, var(--yellow) 0%, rgba(251,238,62,0) 100%),
      linear-gradient(180deg, var(--cream) 0%, #fbdcc8 50%, var(--amber) 100%);
    opacity: 0.9;
  }
</style>
</head>
<body>
  <main class="cover">
    <h1 class="cover__title">
      <span class="cover__title-line cover__title-line--main">Lanternwake</span>
      <span class="cover__title-line cover__title-line--sub">Tales</span>
    </h1>
    <div class="cover__hands" role="img" aria-label="Photograph of two open cupped hands reaching upward, washed in blended green, pink, orange and yellow tones"></div>
  </main>
</body>
</html>
```